Business Cards

Business cards (double-sided) to be handed out to clients and potential clients, with contact details, logo .

Target Market(s)

Small to medium size businesses

Industry/Entity Type

Accountants

Contact Information for Business Card

Brightwater Ledger & Counsel Ltd

Colors

Designer to choose only greyscale colors for use in the design.

Requirements
Must have
• Name, Title, Address, Phone number, Email, Website
Nice to have
• Modern, clean lines, classy
Should not have
• Business cards to be double-sided. Form keeps reverting to single-sided.

```html
<!DOCTYPE html>
<html lang="en">
<head>
<meta charset="utf-8">
<title>Brightwater Ledger &amp; Counsel — Business Card</title>
<link rel="stylesheet" href="https://fonts.googleapis.com/css2?family=Open+Sans:wght@400;700&display=swap">
<style>
  :root {
    --backdrop: #d8d0d1;
    --card: #6f7472;
    --ink-light: #ffffff;
    --ink-dark: #111111;
    --silver: #c3c6c6;
    --silver-deep: #9fa3a3;
    --band: #b4bcba;
  }
  * { margin: 0; padding: 0; box-sizing: border-box; }
  html, body {
    width: 1200px; height: 960px; overflow: hidden;
    background: var(--backdrop);
    font-family: "Open Sans", sans-serif;
  }
  .canvas { position: relative; width: 1200px; height: 960px; }
  .card {
    position: absolute; left: 261px; width: 678px; height: 388px;
    background: var(--card); overflow: hidden;
  }
  .card--front { top: 60px; }
  .card--back { top: 512px; }

  .wordmark { font-weight: 400; text-transform: uppercase; letter-spacing: 0.12em; line-height: 1.2; }
  .card--front .wordmark {
    position: absolute; left: 0; right: 0; top: 140px;
    text-align: center; color: var(--ink-light); font-size: 32px;
  }
  .card--back .wordmark {
    position: absolute; left: 46px; top: 132px;
    color: var(--ink-dark); font-size: 17px;
  }

  .holder { position: absolute; left: 336px; top: 36px; color: var(--ink-light); }
  .holder__name { font-weight: 700; font-size: 23px; letter-spacing: 0.02em; }
  .holder__title { font-size: 15px; color: var(--ink-dark); margin-top: 4px; }

  .contacts { position: absolute; left: 331px; top: 160px; list-style: none; }
  .contacts__item { display: flex; align-items: flex-start; height: 39px; font-size: 15px; color: var(--ink-dark); }
  .contacts__icon {
    width: 27px; height: 27px; border-radius: 50%; background: var(--ink-light);
    display: flex; align-items: center; justify-content: center; flex: none; margin-right: 29px;
  }
  .contacts__text { line-height: 22px; padding-top: 2px; }

  .footer-art { position: absolute; left: 0; top: 0; }
  .website {
    position: absolute; left: 274px; top: 331px;
    font-size: 15px; color: var(--ink-dark);
  }
</style>
</head>
<body>
<main class="canvas">
  <section class="card card--front" aria-label="Card front">
    <p class="wordmark">Brightwater<br>Ledger &amp; Counsel</p>
  </section>

  <section class="card card--back" aria-label="Card back">
    <svg class="footer-art" width="678" height="388" viewBox="0 0 678 388">
      <defs>
        <linearGradient id="silverFill" x1="0" y1="0" x2="1" y2="1">
          <stop offset="0" stop-color="var(--silver)"/>
          <stop offset="1" stop-color="var(--silver-deep)"/>
        </linearGradient>
      </defs>
      <g role="img" aria-label="Embossed silver foil texture">
        <polygon points="0,268 297,268 381,388 0,388" fill="url(#silverFill)"/>
        <polygon points="389,364 678,364 678,388 381,388" fill="url(#silverFill)"/>
      </g>
      <polygon class="accent-band" points="342,314 539,314 578,364 389,364 381,388" fill="var(--band)"/>
    </svg>

    <p class="wordmark">Brightwater<br>Ledger &amp; Counsel</p>

    <div class="holder">
      <h1 class="holder__name">DANIEL HALE</h1>
      <p class="holder__title">Chief Financial Consultant</p>
    </div>

    <ul class="contacts">
      <li class="contacts__item">
        <span class="contacts__icon">
          <svg width="14" height="14" viewBox="0 0 24 24" aria-hidden="true"><path d="M6.6 10.8a15.1 15.1 0 0 0 6.6 6.6l2.2-2.2c.3-.3.7-.4 1-.2 1.1.4 2.3.6 3.6.6.6 0 1 .4 1 1V20c0 .6-.4 1-1 1A17 17 0 0 1 3 4c0-.6.4-1 1-1h3.5c.6 0 1 .4 1 1 0 1.3.2 2.5.6 3.6.1.3 0 .7-.2 1z" fill="#111"/></svg>
        </span>
        <span class="contacts__text">555-014-2298</span>
      </li>
      <li class="contacts__item">
        <span class="contacts__icon" style="font-weight:700;font-size:15px;">@</span>
        <span class="contacts__text">hello@brightwaterledger.com</span>
      </li>
      <li class="contacts__item">
        <span class="contacts__icon">
          <svg width="13" height="15" viewBox="0 0 24 28" aria-hidden="true"><path d="M12 0a10 10 0 0 0-10 10c0 7.5 10 18 10 18s10-10.5 10-18A10 10 0 0 0 12 0zm0 14a4 4 0 1 1 0-8 4 4 0 0 1 0 8z" fill="#111"/></svg>
        </span>
        <span class="contacts__text">48 Harbor Court, Suite 310, Linden<br>NMLS 40517</span>
      </li>
    </ul>

    <p class="website">www.brightwaterledger.com</p>
  </section>
</main>
</body>
</html>
```